Brightvale Fluid Systems Corp Business Cards

Business cards to match the logo.

Company is a start up water technology company that has developed a patented system using centrifugal force to separate waste from municipal waste water to produce crystal clear clean water. Product sell starting at 2 million to governments both in the US and international.

Business cards should have a professional look with the target generally engineers.

Target Market(s)

Engineers, Government officials and investors

Industry/Entity Type

Water Treatment

Contact Information for Business Card

Business cards design will be used for 6 to 8 people with job titles. Can use the quote "If there is magic in the planet, it is contained in water." but not required to use quote. Should follow theme of Logo

Font styles to use
Other font styles liked:
• match logo font

Requirements
Nice to have
• Colors to match Logo. Business cards to match style of flow of Logo.
• Emphasis on clean look not a busy look. Clean flowing water.
Should not have
• Pictures of industrial equipment or wastewater

```html
<!DOCTYPE html>
<html lang="en">
<head>
<meta charset="utf-8">
<title>Brightvale Fluid Systems – Business Cards</title>
<link rel="stylesheet" href="https://fonts.googleapis.com/css2?family=Crimson+Text:wght@400;600;700&display=swap">
<style>
  :root {
    --navy: #0b5178;
    --sky: #2aa7df;
    --white: #ffffff;
    --paper: #fbfbfb;
    --stage: #ececec;
  }
  * { margin: 0; padding: 0; box-sizing: border-box; }
  html, body { width: 1200px; height: 586px; overflow: hidden; }
  body {
    background: var(--stage);
    font-family: "Crimson Text", Georgia, serif;
    position: relative;
  }
  .card {
    position: absolute;
    top: 129px;
    width: 501px;
    height: 301px;
    overflow: hidden;
  }
  .card--front { left: 61px; background: var(--navy); }
  .card--back { left: 619px; background: var(--paper); }

  .wordmark {
    position: absolute;
    left: 0; right: 0;
    text-align: center;
    font-weight: 400;
    text-transform: uppercase;
    line-height: 1;
  }
  .card--front .wordmark { top: 112px; color: var(--white); }
  .card--front .wordmark__main { display: block; font-size: 46px; letter-spacing: 1px; }
  .card--front .wordmark__sub { display: block; font-size: 23px; letter-spacing: 9px; margin-top: 6px; }

  .card--back .wordmark { top: 45px; color: var(--navy); }
  .card--back .wordmark__main { display: block; font-size: 27px; letter-spacing: 0.5px; }
  .card--back .wordmark__sub { display: block; font-size: 13px; letter-spacing: 5px; margin-top: 4px; }

  .wave { position: absolute; left: 0; top: 0; width: 501px; height: 301px; }

  .contact-list {
    position: absolute;
    left: 34px;
    top: 200px;
    list-style: none;
    color: var(--white);
    font-size: 14px;
  }
  .contact-list li { display: flex; align-items: center; height: 26px; }
  .contact-icon { width: 21px; height: 21px; margin-right: 9px; flex: none; }

  .person {
    position: absolute;
    right: 36px;
    top: 183px;
    text-align: right;
    color: var(--white);
  }
  .person__name { font-size: 18px; font-weight: 700; line-height: 1.1; }
  .person__title { font-size: 11.5px; font-weight: 400; }
  .address {
    position: absolute;
    right: 36px;
    top: 251px;
    color: var(--white);
    font-size: 14px;
    font-weight: 700;
  }
</style>
</head>
<body>
  <section class="card card--front" aria-label="Card front">
    <p class="wordmark">
      <span class="wordmark__main">Brightvale</span>
      <span class="wordmark__sub">Fluid Systems</span>
    </p>
  </section>

  <section class="card card--back" aria-label="Card back">
    <p class="wordmark">
      <span class="wordmark__main">Brightvale</span>
      <span class="wordmark__sub">Fluid Systems</span>
    </p>

    <svg class="wave" viewBox="0 0 501 301" aria-hidden="true">
      <path fill="var(--sky)" d="M0 155 C70 178 140 186 210 176 C300 160 380 105 445 108 C470 109 490 113 501 117 L501 301 L0 301 Z"/>
      <path fill="var(--navy)" d="M0 167 C70 186 140 192 210 183 C300 168 380 122 445 122 C470 122 490 124 501 127 L501 301 L0 301 Z"/>
    </svg>

    <ul class="contact-list">
      <li>
        <svg class="contact-icon" viewBox="0 0 20 20" aria-hidden="true">
          <circle cx="10" cy="10" r="10" fill="var(--white)"/>
          <path fill="var(--navy)" d="M4.5 8.2c0-1.6 2.5-2.7 5.5-2.7s5.5 1.1 5.5 2.7v.9h-2.6v-1.3c-.8-.3-1.8-.4-2.9-.4s-2.1.1-2.9.4v1.3H4.5z M6.6 9.5h6.8l1.2 4.8H5.4z"/>
        </svg>
        +612 9481 2206
      </li>
      <li>
        <svg class="contact-icon" viewBox="0 0 20 20" aria-hidden="true">
          <circle cx="10" cy="10" r="10" fill="var(--white)"/>
          <path fill="var(--navy)" d="M6.5 4.8h7v3h-7z M4.5 8.3h11v5h-2v-1.6h-7v1.6h-2z M7 12.3h6v3H7z"/>
        </svg>
        +612 9481 2207
      </li>
      <li>
        <svg class="contact-icon" viewBox="0 0 20 20" aria-hidden="true">
          <circle cx="10" cy="10" r="10" fill="var(--white)"/>
          <rect x="4.5" y="6.3" width="11" height="7.6" fill="var(--navy)"/>
          <path d="M4.8 6.6 10 10.8l5.2-4.2" fill="none" stroke="var(--white)" stroke-width="1"/>
        </svg>
        info@brightvalefluid.com
      </li>
    </ul>

    <div class="person">
      <p class="person__name">Marion Keller</p>
      <p class="person__title">Owner / Founder</p>
    </div>
    <p class="address">412 Harbor Row, Eastfield NY 11520</p>
  </section>
</body>
</html>
```